business card and stationary
Byte Haven Works
Modern
Martin Okonedo
Owner
2738 Larkin Avenue
Green Cove Springs FL 32043
bytehavenworks@mailnest.example
www.bytehavenworks.example
I don't want the address on the business card.
logo .ai file

```html
<!DOCTYPE html>
<html lang="en">
<head>
<meta charset="utf-8">
<title>Byte Haven Works – Stationery</title>
<link href="https://fonts.googleapis.com/css2?family=Open+Sans:wght@400;600;800&display=swap" rel="stylesheet">
<style>
  :root{
    --board:#e4e6e8;
    --paper:#ffffff;
    --ink:#1d2733;
    --muted:#7b848d;
    --blue:#1e5fbf;
    --blue-deep:#0c2f6b;
    --blue-light:#4f93e6;
    --black:#141517;
    --shadow:0 2px 6px rgba(0,0,0,.18);
  }
  *{box-sizing:border-box;margin:0;padding:0}
  html,body{width:1200px;height:427px;overflow:hidden}
  body{background:var(--board);font-family:"Open Sans",sans-serif;color:var(--ink);position:relative}
  .brand{font-weight:800;text-transform:uppercase;letter-spacing:.5px;color:var(--ink);white-space:nowrap;display:flex;align-items:center;gap:6px}
  .brand .mark{display:inline-block;background:var(--blue);flex:none}
  .board-title{position:absolute;left:22px;top:118px}
  .board-title .brand{font-size:15px}
  .board-title .brand .mark{width:12px;height:12px}
  .board-title .caption{font-size:10px;color:var(--muted);margin-top:14px}
  .sheet{position:absolute;background:var(--paper);box-shadow:var(--shadow);overflow:hidden}
  .card{left:26px;top:269px;width:202px;height:115px}
  .card .brand{position:absolute;left:12px;top:14px;font-size:12px}
  .card .brand .mark{width:9px;height:9px}
  .card .person{position:absolute;left:12px;top:50px;font-size:8px;font-weight:600;white-space:nowrap}
  .card .role{font-weight:400;color:var(--muted);font-size:7px}
  .card .contact{position:absolute;left:94px;top:50px;font-size:5px;line-height:9px;color:var(--muted);white-space:nowrap}
  .card .band{position:absolute;left:0;bottom:0;width:100%;height:18px}
  .letterhead{top:26px;width:266px;height:345px}
  .letterhead.one{left:353px}
  .letterhead.two{left:643px}
  .letterhead .brand{position:absolute;left:14px;top:27px;font-size:10px;gap:5px}
  .letterhead .brand .mark{width:8px;height:8px}
  .letterhead .contact{position:absolute;left:172px;top:22px;font-size:5px;line-height:7.5px;color:var(--muted);white-space:nowrap}
  .letterhead.two .brand{left:50%;transform:translateX(-50%)}
  .letterhead .band{position:absolute;left:0;bottom:0;width:100%;height:26px}
  .label{position:absolute;font-size:7px;color:var(--muted);white-space:nowrap}
  .envelope{position:absolute;box-shadow:var(--shadow);overflow:hidden}
  .envelope svg.flap{position:absolute;inset:0;width:100%;height:100%}
  .envelope .brand{position:absolute;font-size:11px}
  .envelope .brand .mark{width:8px;height:8px}
  .env-black{left:919px;top:36px;width:257px;height:125px;background:var(--black)}
  .env-black .brand{left:50%;top:44px;transform:translateX(-50%);color:#fff}
  .env-black .brand .mark{background:#fff}
  .env-blue{left:943px;top:72px;width:233px;height:168px;background:linear-gradient(180deg,var(--blue-light),var(--blue) 45%,var(--blue-deep))}
  .env-blue .brand{left:50%;top:58px;transform:translateX(-50%);color:#fff}
  .env-blue .brand .mark{background:#fff}
  .env-white{left:924px;top:180px;width:252px;height:144px;background:var(--paper)}
  .env-front{left:941px;top:259px;width:235px;height:137px;background:var(--paper)}
  .env-front .brand{left:12px;top:12px}
  .env-front .band{position:absolute;left:0;bottom:0;width:100%;height:16px}
</style>
</head>
<body>

<header class="board-title">
  <div class="brand"><span class="mark"></span>Byte Haven Works</div>
  <p class="caption">Stationery Concepts</p>
</header>

<section class="sheet card">
  <div class="brand"><span class="mark"></span>Byte Haven Works</div>
  <div class="person">Martin Okonedo<br><span class="role">Owner</span></div>
  <div class="contact">(904) 555-0148<br>bytehavenworks@mailnest.example<br>www.bytehavenworks.example</div>
  <svg class="band" viewBox="0 0 202 18" preserveAspectRatio="none">
    <path d="M0 10 Q100 2 202 8 L202 18 L0 18Z" fill="var(--blue)"/>
    <path d="M0 14 Q110 6 202 12 L202 18 L0 18Z" fill="var(--blue-deep)"/>
  </svg>
</section>

<section class="sheet letterhead one">
  <div class="brand"><span class="mark"></span>Byte Haven Works</div>
  <div class="contact">2738 Larkin Avenue<br>Green Cove Springs FL 32043<br>bytehavenworks@mailnest.example<br>www.bytehavenworks.example</div>
  <svg class="band" viewBox="0 0 266 26" preserveAspectRatio="none">
    <path d="M0 16 Q130 4 266 12 L266 26 L0 26Z" fill="var(--blue)"/>
    <path d="M0 21 Q140 10 266 18 L266 26 L0 26Z" fill="var(--blue-deep)"/>
  </svg>
</section>
<p class="label" style="left:452px;top:384px">Letterhead Option 1</p>

<section class="sheet letterhead two">
  <div class="brand"><span class="mark"></span>Byte Haven Works</div>
  <svg class="band" viewBox="0 0 266 26" preserveAspectRatio="none">
    <path d="M0 16 Q130 4 266 12 L266 26 L0 26Z" fill="var(--blue)"/>
    <path d="M0 21 Q140 10 266 18 L266 26 L0 26Z" fill="var(--blue-deep)"/>
  </svg>
</section>
<p class="label" style="left:742px;top:384px">Letterhead Option 2</p>

<section class="envelope env-black">
  <svg class="flap" viewBox="0 0 257 125" preserveAspectRatio="none"><path d="M0 0 L128 70 L257 0" fill="none" stroke="#2c2e31" stroke-width="1.5"/></svg>
  <div class="brand"><span class="mark"></span>Byte Haven Works</div>
</section>

<section class="envelope env-blue">
  <svg class="flap" viewBox="0 0 233 168" preserveAspectRatio="none"><path d="M0 0 L116 50 L233 0" fill="none" stroke="rgba(255,255,255,.35)" stroke-width="1.5"/></svg>
  <div class="brand"><span class="mark"></span>Byte Haven Works</div>
</section>

<section class="envelope env-white">
  <svg class="flap" viewBox="0 0 252 144" preserveAspectRatio="none">
    <path d="M0 0 L126 60 L252 0" fill="none" stroke="#d3d6d9" stroke-width="1.2"/>
    <path d="M0 144 L100 70 M252 144 L152 70" fill="none" stroke="#e2e4e6" stroke-width="1"/>
  </svg>
</section>

<section class="envelope env-front">
  <div class="brand"><span class="mark"></span>Byte Haven Works</div>
  <svg class="band" viewBox="0 0 235 16" preserveAspectRatio="none">
    <path d="M0 9 Q120 2 235 7 L235 16 L0 16Z" fill="var(--blue)"/>
    <path d="M0 13 Q130 6 235 11 L235 16 L0 16Z" fill="var(--blue-deep)"/>
  </svg>
</section>
<p class="label" style="left:1040px;top:402px">Envelope Front and Back</p>

</body>
</html>
```